Harvest Gate Fellowship Network needs a fresh new web design

We are an up and coming multicultural church that aims to bring people into a life changing encounter with God. We need a fresh and inviting website in order to increase our internet presence and make us easier to connect with.
Here are some of the basic requirements for the site:
• Clearly displayed address, service times, and contact info
• A staff profile page
• An area for a calendar with upcoming events and their details
• Social media buttons
• Group pages for the different ministries (youth, children’s church, men, etc…)
• An area for donations and eCommerce
• A resources page for assorted media (podcasts, sermons, videos, etc.…)
• An area for prayer requests.

Industry/Entity Type

Church

```html
<!DOCTYPE html>
<html lang="en">
<head>
<meta charset="utf-8">
<title>Staff Profile – Harvest Gate Fellowship Network</title>
<link href="https://fonts.googleapis.com/css2?family=Lato:wght@300;400;700;900&display=swap" rel="stylesheet">
<style>
:root{
  --navy:#1b0f96;
  --navy-deep:#170c8a;
  --gold:#e6c20c;
  --gold-text:#e2b81c;
  --gold-link:#d9a900;
  --paper:#f1f1f1;
  --ink:#333;
  --body:#555;
  --muted:#999;
  --icon:#a8a8a8;
  --foot-head:#dcdcf7;
  --foot-text:#bcbdf0;
}
*{box-sizing:border-box;margin:0;padding:0}
html,body{width:950px;height:1200px;overflow:hidden}
body{font-family:"Lato",Arial,sans-serif;background:var(--paper);color:var(--ink);position:relative}
.abs{position:absolute}

/* top bar */
.topbar{left:0;top:0;width:950px;height:32px;background:var(--navy);color:#fff}
.topbar .tagline{left:79px;top:10px;font-size:11px}
.topbar .schedule-label{left:583px;top:10px;font-size:11px}
.topbar .schedule-rule{left:729px;top:6px;width:2px;height:20px;background:#fff}
.topbar .schedule-times{left:738px;top:5px;font-size:9.5px;line-height:11px}

/* header */
.header{left:0;top:32px;width:950px;height:91px;background:#fff}
.brand{left:80px;top:16px;display:flex;align-items:center;gap:8px}
.brand-dot{width:40px;height:40px;border-radius:50%;background:var(--gold);flex:none}
.brand-name{font-size:15px;font-weight:700;color:var(--navy);line-height:17px;width:150px}
.info{top:19px;text-align:right;font-size:11px;color:var(--body);line-height:12px}
.info h3{font-size:13px;font-weight:700;color:#555;margin-bottom:4px}
.info a{display:block;color:var(--gold-link);font-size:9.5px;text-decoration:none;margin-top:2px}
.info-rule{top:21px;width:2px;height:50px;background:#ddd}
.social-dot{border-radius:50%;background:var(--icon);display:flex;align-items:center;justify-content:center}
.social-dot span{display:block;width:40%;height:40%;border-radius:50%;background:#fff}
.header .social-dot{left:850px;width:21px;height:21px}

/* nav */
.nav{left:0;top:123px;width:950px;height:32px;background:var(--gold)}
.nav ul{list-style:none;display:flex;justify-content:space-between;margin:0 79px;height:32px;align-items:center}
.nav li{font-size:11.5px;color:#333;position:relative;padding:0 12px}
.nav li+li::before{content:"";position:absolute;left:-16px;top:2px;width:1px;height:10px;background:#c9a300}

/* banner */
.banner{left:0;top:155px;width:950px;height:79px;background:radial-gradient(ellipse at 60% 40%,#6b4d14 0%,#3e2b0c 55%,#241806 100%)}
.banner .crumbs{left:79px;top:22px;font-size:10.5px;color:#eee}
.banner .crumbs b{color:#fff;font-weight:400}
.banner h1{left:79px;top:36px;font-size:19px;font-weight:900;color:#fff}

/* intro */
.intro{left:0;top:278px;width:950px;text-align:center;font-size:11.5px;color:var(--body);line-height:17px}
.section-title{left:88px;top:335px;width:774px;text-align:center;font-size:18px;font-weight:300;color:var(--gold-text);border-bottom:1px solid #d9c77a;padding-bottom:4px}

/* staff */
.staff{left:88px;width:157px;text-align:center}
.staff .photo{width:157px;height:127px;border:1px solid #e2e2e2;background:radial-gradient(circle at 50% 45%,#fff 35%,#e4e4e4 100%)}
.staff .photo.portrait{background:radial-gradient(circle at 50% 45%,#c97b3c 0%,#a85a22 70%,#8e4a1b 100%);border-color:#ccc}
.staff h2{font-size:14px;font-weight:400;color:#222;margin-top:13px;text-transform:uppercase;line-height:17px}
.staff .role{font-size:10px;font-style:italic;color:var(--muted);line-height:13px}
.staff p{font-size:10.5px;color:var(--body);line-height:15px;margin-top:5px}
.staff .links{display:flex;justify-content:center;gap:6px;margin-top:13px}
.staff .links .social-dot{width:19px;height:19px;background:#c4c4c4}

/* footer */
.footer{left:0;top:962px;width:950px;height:238px;background:var(--navy-deep)}
.footer h4{font-size:15px;font-weight:300;color:var(--foot-head);text-transform:uppercase;margin-bottom:9px}
.fcol{top:32px;font-size:10.5px;color:var(--foot-text);line-height:14px}
.contact-line{display:flex;align-items:center;gap:7px;margin-top:2px;font-size:11px;line-height:16px}
.links-list{display:flex;gap:14px;list-style:none}
.links-list ul{list-style:none}
.links-list li{line-height:19px}
.email-field{width:180px;height:27px;background:#fff;border-radius:2px;margin-top:8px;font-size:10.5px;color:#bbb;padding:7px 10px}
.subscribe{width:74px;height:27px;background:var(--gold);color:#333;font-size:10.5px;border-radius:2px;margin-top:8px;text-align:center;line-height:27px}
.footer .social-row{display:flex;gap:6px;margin-top:5px}
.footer .social-row .social-dot{width:25px;height:25px;background:#c8c8e6}
.footer .social-row .social-dot span{background:var(--navy-deep)}
.footer .rule{left:79px;top:178px;width:792px;height:1px;background:#2d22a8}
.copyright{left:0;top:192px;width:950px;text-align:center;font-size:9.5px;color:#b0b1e6}
</style>
</head>
<body>

<div class="abs topbar">
  <div class="abs tagline">A house of prayer for all nations, where the love, the presence and the power of God are real.</div>
  <div class="abs schedule-label">SUNDAY SERVICE SCHEDULE</div>
  <div class="abs schedule-rule"></div>
  <div class="abs schedule-times">09:00 A.M. | Sunday School<br>10:30 A.M. | Convergent Service</div>
</div>

<header class="abs header">
  <div class="abs brand">
    <div class="brand-dot"></div>
    <div class="brand-name">Harvest Gate Fellowship Network</div>
  </div>
  <div class="abs info" style="right:497px">
    <h3>Donate</h3>Lorem Ipsum is simply<br>dummy text of the printing<a href="#">Donate Now »</a>
  </div>
  <div class="abs info-rule" style="left:468px"></div>
  <div class="abs info" style="right:274px">
    <h3>Request Prayer</h3>Lorem Ipsum is simply dummy text<br>of the printing and typesetting industry.<a href="#">Request Now »</a>
  </div>
  <div class="abs info-rule" style="left:691px"></div>
  <div class="abs info" style="right:133px">
    <h3>Address</h3>Harvest Gate<br>City, Location<a href="#">Contact »</a>
  </div>
  <div class="abs info-rule" style="left:832px"></div>
  <div class="abs social-dot" style="top:23px" aria-label="Social link"><span></span></div>
  <div class="abs social-dot" style="top:48px" aria-label="Social link"><span></span></div>
</header>

<nav class="abs nav">
  <ul>
    <li>Home</li><li>About</li><li>Staff Profile</li><li>News and Events</li><li>Worship &amp; Services</li><li>Groups</li><li>Shop</li><li>Resources</li><li>Contact</li>
  </ul>
</nav>

<div class="abs banner" role="img" aria-label="Soft-focus golden wheat field banner">
  <div class="abs crumbs">Home &gt; <b>Staff Profile</b></div>
  <h1 class="abs">Staff Profile</h1>
</div>

<div class="abs intro">Lorem Ipsum is simply dummy text of the printing and typesetting industry.<br>Lorem Ipsum has been the industry's standard dummy text ever since the 1500s, when an unknown printer took a galley of type and scrambled it to make a type.</div>
<div class="abs section-title">STAFF PROFILE</div>

<div class="abs staff" style="left:88px;top:386px">
  <div class="photo portrait" role="img" aria-label="Portrait photo of Daniel Mensah"></div>
  <h2>Daniel Mensah</h2><div class="role">Designation</div>
  <p>Lorem Ipsum is simply dummy text of the printing and typesetting industry industry's standard.</p>
  <div class="links"><div class="social-dot"><span></span></div><div class="social-dot"><span></span></div></div>
</div>
<div class="abs staff" style="left:294px;top:386px">
  <div class="photo" role="img" aria-label="Staff photo placeholder"></div>
  <h2>John Doe</h2><div class="role">Designation</div>
  <p>Lorem Ipsum is simply dummy text of the printing and typesetting industry industry's standard.</p>
  <div class="links"><div class="social-dot"><span></span></div><div class="social-dot"><span></span></div></div>
</div>
<div class="abs staff" style="left:500px;top:386px">
  <div class="photo" role="img" aria-label="Staff photo placeholder"></div>
  <h2>John Doe</h2><div class="role">Designation</div>
  <p>Lorem Ipsum is simply dummy text of the printing and typesetting industry industry's standard.</p>
  <div class="links"><div class="social-dot"><span></span></div><div class="social-dot"><span></span></div></div>
</div>
<div class="abs staff" style="left:706px;top:386px">
  <div class="photo" role="img" aria-label="Staff photo placeholder"></div>
  <h2>John Doe</h2><div class="role">Designation</div>
  <p>Lorem Ipsum is simply dummy text of the printing and typesetting industry industry's standard.</p>
  <div class="links"><div class="social-dot"><span></span></div><div class="social-dot"><span></span></div></div>
</div>

<div class="abs staff" style="left:88px;top:662px">
  <div class="photo" role="img" aria-label="Staff photo placeholder"></div>
  <h2>John Doe</h2><div class="role">Designation</div>
  <p>Lorem Ipsum is simply dummy text of the printing and typesetting industry industry's standard.</p>
  <div class="links"><div class="social-dot"><span></span></div><div class="social-dot"><span></span></div></div>
</div>
<div class="abs staff" style="left:294px;top:662px">
  <div class="photo" role="img" aria-label="Staff photo placeholder"></div>
  <h2>John Doe</h2><div class="role">Designation</div>
  <p>Lorem Ipsum is simply dummy text of the printing and typesetting industry industry's standard.</p>
  <div class="links"><div class="social-dot"><span></span></div><div class="social-dot"><span></span></div></div>
</div>
<div class="abs staff" style="left:500px;top:662px">
  <div class="photo" role="img" aria-label="Staff photo placeholder"></div>
  <h2>John Doe</h2><div class="role">Designation</div>
  <p>Lorem Ipsum is simply dummy text of the printing and typesetting industry industry's standard.</p>
  <div class="links"><div class="social-dot"><span></span></div><div class="social-dot"><span></span></div></div>
</div>
<div class="abs staff" style="left:706px;top:662px">
  <div class="photo" role="img" aria-label="Staff photo placeholder"></div>
  <h2>John Doe</h2><div class="role">Designation</div>
  <p>Lorem Ipsum is simply dummy text of the printing and typesetting industry industry's standard.</p>
  <div class="links"><div class="social-dot"><span></span></div><div class="social-dot"><span></span></div></div>
</div>

<footer class="abs footer">
  <div class="abs fcol" style="left:79px">
    <h4>Contact Us</h4>
    Harvest Gate<br>Location, city<br>State Name, Country
    <div class="contact-line" style="margin-top:7px">
      <svg width="13" height="12" viewBox="0 0 13 12"><path d="M2 1 L4.5 0.5 L5.5 3.5 L4 4.5 Q5.5 7.5 8 8.5 L9 7 L12 8 L11.5 10.5 Q6 11 2.5 6.5 Q0.5 3.5 2 1Z" fill="#c8c8e6"/></svg>
      +1 555-014-2290
    </div>
    <div class="contact-line">
      <svg width="13" height="10" viewBox="0 0 13 10"><rect x="0.5" y="0.5" width="12" height="9" fill="#c8c8e6"/><path d="M0.5 0.5 L6.5 5.5 L12.5 0.5" fill="none" stroke="#170c8a" stroke-width="1.2"/></svg>
      hello@harvestgatenet.org
    </div>
  </div>
  <div class="abs fcol" style="left:254px">
    <h4>Communities We Serve</h4>
    <div class="links-list">
      <ul><li>• Lorem Ipsum</li><li>• Dummy Links</li><li>• More dummy</li><li>• Sample Text</li><li>• More samples</li></ul>
      <ul><li>• type text dummy</li><li>• Lorem Ipsum</li></ul>
    </div>
  </div>
  <div class="abs fcol" style="left:474px">
    <h4>Newsletter</h4>
    Enter your email below to get notified
    <div class="email-field">Your Email</div>
    <div class="subscribe">Subscribe</div>
  </div>
  <div class="abs fcol" style="left:694px">
    <h4>Connect With Us</h4>
    Stay connected for the latest updates at<br>Harvest Gate Fellowship
    <div class="social-row"><div class="social-dot"><span></span></div><div class="social-dot"><span></span></div></div>
  </div>
  <div class="abs rule"></div>
  <div class="abs copyright">Copyright © 2014. All rights reserved. Harvest Gate.</div>
</footer>

</body>
</html>
```